Wordpress Web Design For Midlifers.com

We're looking to update the design for www.midlifers.com. The website provides news and views for people aged 50 plus.

We want to use Wordpress as the content management tool and incorporate mailchimp to manage subscribers to our monthly newsletter.

In terms of design, we're looking for something simple and straightforward, we quite like the elder hub site, so something like that would be good. http://www.elderhub.org.uk
Updates

Project Deadline Extended
Reason: Dear All, Due to the Xmas break in the UK I've decided to extend the deadline by 7 days. Thanks for all your submissions, we will be making a decision shortly. Please note, as per the original brief, we are only interested in fully coded sites uploaded to our hosting provider. Please withdraw your design if you are not able to offer this complete solution. Thanks and good wishes to all!

Requirements
Must have
• Fully working wordpress templates that allow us to easily manage the website content. Easy for readers to use, navigate and read the content.
• Ideally a'turnkey' solution - the website built and ready for us to use wordpress to populate with content.

```html
<!DOCTYPE html>
<html lang="en">
<head>
<meta charset="utf-8">
<title>Travel – Midlifers.com</title>
<link href="https://fonts.googleapis.com/css2?family=Open+Sans:wght@400;600;700&family=Montserrat:wght@500;600;700&family=Lora:wght@700&display=swap" rel="stylesheet">
<style>
:root{
  --green:#6aa21c;
  --green-dark:#4f8a10;
  --green-light:#8cc63f;
  --text:#666;
  --heading:#333;
  --page:#f3f3f3;
  --line:#dcdcdc;
  --white:#fff;
  --btn:#e4e4e4;
}
*{box-sizing:border-box;margin:0;padding:0}
html,body{width:1200px;height:2210px;overflow:hidden}
body{position:relative;background:var(--page);font-family:"Open Sans",Arial,sans-serif;color:var(--text)}
.site-header{position:absolute;left:0;top:0;width:1200px;height:175px;background:var(--white)}
.brand{position:absolute;left:141px;top:30px;display:flex;align-items:center;gap:14px}
.brand-mark{width:62px;height:62px;border-radius:50%;background:var(--green)}
.brand-name{font-family:"Montserrat",sans-serif;font-weight:600;font-size:22px;color:#444;line-height:1}
.header-ad{position:absolute;left:378px;top:20px;width:680px;height:82px;background:linear-gradient(#2a6fb0,#15457c);color:#fff;display:flex;align-items:center}
.header-ad .ad-photo{width:140px;height:66px;margin-left:10px;background:linear-gradient(90deg,#e8d9b5,#c6b080)}
.header-ad .ad-copy{flex:1;text-align:center}
.header-ad .ad-copy strong{display:block;font-family:"Montserrat",sans-serif;font-size:32px;font-weight:700;line-height:1.05}
.header-ad .ad-copy span{font-size:21px}
.header-ad .ad-badge{width:160px;height:70px;margin-right:8px;background:#fff;display:flex;align-items:center;gap:8px;padding:6px}
.header-ad .ad-badge i{width:40px;height:40px;background:#8b1e3f;display:block}
.header-ad .ad-badge b{color:#1d3f7a;font-size:15px;line-height:1.1}
.main-nav{position:absolute;left:141px;top:122px;width:916px;height:46px;display:flex;border:1px solid var(--line);background:var(--white)}
.main-nav a{flex:1 1 auto;text-align:center;line-height:44px;font-size:16px;color:#333;text-decoration:none;border-right:1px solid var(--line)}
.main-nav a:last-child{border-right:0}
.main-nav a.current{color:var(--green);background:#f6f6f6}
.hero{position:absolute;left:141px;top:181px;width:608px;height:173px;background:linear-gradient(180deg,#8fd3ec 0%,#cfeef6 55%,#f2eedd 100%);border:1px solid var(--line)}
.hero h1{position:absolute;left:22px;bottom:10px;font-family:"Lora",serif;font-size:28px;color:#111;letter-spacing:1px}
.posts{position:absolute;left:141px;top:385px;width:608px;display:grid;grid-template-columns:279px 279px;column-gap:50px;row-gap:0}
.post{height:366px}
.post h2{font-family:"Montserrat",sans-serif;font-weight:600;font-size:15.5px;color:var(--green);text-transform:uppercase;line-height:21px}
.post .thumb{width:279px;height:166px;margin-top:12px}
.post p{font-size:13.5px;line-height:22px;margin-top:16px;height:66px;overflow:hidden}
.read-more{display:inline-block;margin-top:12px;background:var(--btn);color:#777;font-size:11px;font-weight:600;padding:4px 9px;letter-spacing:.5px}
.pager{position:absolute;left:141px;top:1872px;display:flex;gap:14px}
.pager a{display:flex;align-items:center;gap:10px;border:1px solid var(--green);background:#fff;height:42px;padding:0 12px 0 0;color:#333;font-size:11px;font-weight:700;line-height:13px;text-decoration:none}
.pager a i{width:40px;height:40px;background:var(--green);display:flex;align-items:center;justify-content:center}
.sidebar{position:absolute;left:778px;top:186px;width:280px}
.search{height:38px;border-radius:19px;background:#fff;border:1px solid var(--line);display:flex;align-items:center;justify-content:space-between;padding:0 8px 0 16px;font-size:12px;color:#999}
.search i{width:22px;height:22px;border-radius:50%;background:var(--green);display:flex;align-items:center;justify-content:center}
.widget{background:#fff;border:1px solid var(--line);margin-top:24px}
.widget-title{background:linear-gradient(var(--green-light),var(--green));color:#fff;font-family:"Lora",serif;font-size:19px;text-transform:uppercase;padding:8px 12px}
.widget-body{padding:12px 10px}
.field{height:32px;border:1px solid var(--line);border-radius:3px;font-size:12px;color:#888;line-height:30px;padding-left:10px;margin-bottom:10px}
.tiny{font-size:11px;color:#666}
.row{display:flex;gap:16px;align-items:center}
.btn-submit{display:inline-block;background:linear-gradient(var(--green-light),var(--green-dark));color:#fff;font-weight:700;font-size:15px;padding:4px 14px;border-radius:3px;margin:10px 0}
.news-head{display:flex;align-items:center;gap:12px;font-family:"Lora",serif;font-size:22px;color:#333}
.news-text{font-size:13px;line-height:20px;margin:10px 0}
.ad-slide{margin-top:26px;height:234px;background:linear-gradient(#8ec1e8,#7a9a5a);position:relative}
.ad-slide span{position:absolute;left:50%;bottom:10px;transform:translateX(-50%);background:#2b6cb0;color:#fff;font-size:13px;padding:4px 22px;white-space:nowrap}
.ad-travel{margin-top:22px;height:562px;background:#fff;border:1px solid var(--line);text-align:center;overflow:hidden}
.ad-travel .logo{font-family:"Montserrat",sans-serif;font-size:30px;color:#1f76b6;margin-top:10px}
.ad-travel .tag{font-size:9px;color:#333}
.ad-travel .q{font-weight:700;color:#1d4f8a;font-size:19px;margin-top:12px}
.ad-travel .scene{height:380px;margin-top:10px;background:linear-gradient(#6fb6e6,#4a8dc7 50%,#d9c8a6);position:relative}
.ad-travel .was{position:absolute;left:0;right:0;top:92px;color:#c00;font-weight:700;font-size:22px;text-decoration:line-through}
.ad-travel .now{position:absolute;left:0;right:0;top:125px;color:#fff;font-weight:700;font-size:56px;font-family:"Montserrat",sans-serif}
.ad-travel .off{position:absolute;right:24px;top:190px;width:76px;height:76px;border-radius:50%;background:#e8a020;color:#fff;font-weight:700;font-size:15px;line-height:18px;display:flex;flex-direction:column;align-items:center;justify-content:center;white-space:nowrap}
.ad-travel .sub{position:absolute;left:80px;top:10px;color:#111;font-weight:700;font-size:14px;text-align:right;width:180px;line-height:17px}
.social-box{margin-top:24px;height:307px;background:#fff;border:1px solid var(--line);padding:8px}
.social-box .t{font-size:11px;font-weight:700;color:#3b5998}
.social-box .who{display:flex;gap:8px;align-items:center;margin:8px 0;font-size:11px}
.social-box .who i{width:40px;height:40px;border-radius:50%;background:var(--green);display:block}
.faces{display:grid;grid-template-columns:repeat(5,44px);gap:6px;margin-top:8px}
.faces i{height:44px;background:#b9a58e;display:block}
.site-footer{position:absolute;left:0;top:2073px;width:1200px;height:137px;background:linear-gradient(var(--green),var(--green-dark));color:#fff}
.footer-nav{position:absolute;left:0;right:0;top:22px;text-align:center;font-size:13px}
.footer-nav a{color:#fff;text-decoration:none}
.footer-nav em{font-style:normal;margin:0 8px}
.footer-rule{position:absolute;left:141px;right:142px;top:62px;border-top:1px solid rgba(255,255,255,.3)}
.copyright{position:absolute;left:141px;top:86px;font-size:12px}
.follow{position:absolute;right:142px;top:78px;display:flex;gap:10px}
.follow i{width:34px;height:34px;border-radius:50%;background:#fff;display:block}
</style>
</head>
<body>
<header class="site-header">
  <div class="brand"><span class="brand-mark"></span><span class="brand-name">Midlifers.com</span></div>
  <div class="header-ad">
    <div class="ad-photo" role="img" aria-label="Photo of a family meal"></div>
    <div class="ad-copy"><strong>Over 50’s Life Plan</strong><span>Life cover from just 33p a day</span></div>
    <div class="ad-badge"><i></i><b>Harbourline<br>Mutual</b></div>
  </div>
  <nav class="main-nav">
    <a>Home</a><a>About</a><a class="current">Travel</a><a>Health</a><a>Hobbies</a><a>Lifestyle</a><a>Insurance</a><a>Legal</a><a>Competitions</a><a>Survey</a><a>Contact</a>
  </nav>
</header>

<section class="hero" role="img" aria-label="Tropical beach with a jetty and palm trees"><h1>TRAVEL</h1></section>

<main class="posts">
  <article class="post"><h2>The Westcountry farm pork pie now boarding the 1206 ...</h2><div class="thumb" role="img" aria-label="Modern passenger train at a platform" style="background:linear-gradient(#a8b9c9,#4a4f6a)"></div><p>Rail company that runs iconic train lines west from London commits to source food from the counties it crosses in a bid to end</p><span class="read-more">READ MORE</span></article>
  <article class="post"><h2>The Voyager’s Sea Guide</h2><div class="thumb" role="img" aria-label="Cover of a cruise travel guide" style="background:linear-gradient(#fff 0%,#fff 55%,#7a3f9a 55%)"></div><p>‘The Voyager’s Sea Guide’ is a must-read for those who are considering booking a cruise, but holding off due to</p><span class="read-more">READ MORE</span></article>
  <article class="post"><h2>Home from home with Wexford Lodges</h2><div class="thumb" role="img" aria-label="Country house with garden" style="background:linear-gradient(#dfe6ea,#9aa98a 60%,#6f8a4a)"></div><p>Wouldn’t it be great to have a network of friends, who live in fabulous houses, and on whom you can drop in and stay a night</p><span class="read-more">READ MORE</span></article>
  <article class="post"><h2>Daniel Gowan’s travel tips for Australia</h2><div class="thumb" role="img" aria-label="City skyline across a river at dusk" style="background:linear-gradient(#e9d2b8,#6f8fb8 55%,#2a4a7a)"></div><p>England cricketing legend Daniel Gowan had the privilege of touring some of the most fantastic countries in the world</p><span class="read-more">READ MORE</span></article>
  <article class="post"><h2>In the driving seat</h2><div class="thumb" role="img" aria-label="Older woman driving a car" style="background:linear-gradient(90deg,#c8d2d8,#2f8fb8 60%,#2a2a2a)"></div><p>For many of us, driving is a way to maintain our independence and freedom. However, negative stories in the media</p><span class="read-more">READ MORE</span></article>
  <article class="post"><h2>Garden Tours</h2><div class="thumb" role="img" aria-label="Colourful flower garden" style="background:linear-gradient(#6fa3d0,#4f8a2a 45%,#a84a7a)"></div><p>Enjoy wonderful gardens and wild plants worldwide on an expert led tour. There are many horticultural wonders to behold!</p><span class="read-more">READ MORE</span></article>
  <article class="post"><h2>UK tours by coach or train</h2><div class="thumb" role="img" aria-label="Green valley with stone walls" style="background:linear-gradient(#b9d4ea,#7fae3f 40%,#4f7a22)"></div><p>Travelling around the UK is so enjoyable, no flying, no passports, just sit back and take in the scenery, with many excursions</p><span class="read-more">READ MORE</span></article>
  <article class="post"><h2>Top tips for touring holidays</h2><div class="thumb" role="img" aria-label="Coach on a mountain road" style="background:linear-gradient(#9ec3e2,#e8ecef 55%,#6a7a5a)"></div><p>Some really useful suggestions to get your tour off to a great start. What to consider before you head off on the trip.</p><span class="read-more">READ MORE</span></article>
</main>

<div class="pager">
  <a><i><svg width="18" height="18" viewBox="0 0 18 18"><path d="M11 3 5 9l6 6" fill="none" stroke="#fff" stroke-width="2.5"/></svg></i>OLDER<br>ARTICLE</a>
  <a><i><svg width="20" height="18" viewBox="0 0 20 18"><path d="M2 9 10 2l8 7M5 8v8h10V8" fill="none" stroke="#fff" stroke-width="2"/></svg></i>BACK TO<br>HOME</a>
</div>

<aside class="sidebar">
  <div class="search">Search<i><svg width="10" height="10" viewBox="0 0 10 10"><path d="M3 1l4 4-4 4" fill="none" stroke="#fff" stroke-width="2"/></svg></i></div>
  <section class="widget">
    <h3 class="widget-title">Login</h3>
    <div class="widget-body">
      <div class="field">Username</div><div class="field">Password</div>
      <div class="row tiny"><span>☑ Remember Me</span><span>Forgot Your Password</span></div>
      <span class="btn-submit">SUBMIT</span>
      <div class="tiny">✔ Register here</div>
    </div>
  </section>
  <section class="widget">
    <h3 class="widget-title">Keep up to date</h3>
    <div class="widget-body">
      <div class="news-head"><svg width="36" height="30" viewBox="0 0 36 30"><rect x="2" y="6" width="32" height="22" fill="#eee" stroke="#999"/><path d="M2 6l16 12L34 6" fill="none" stroke="#999"/></svg>Newsletter!</div>
      <p class="news-text">Sign up for our fortnightly newsletter to stay on top of the latest from Midlifers.com.</p>
      <div class="field">Enter your email_id</div>
      <span class="btn-submit">SUBMIT</span>
    </div>
  </section>
  <div class="ad-slide" role="img" aria-label="Winding water slide in a park"><span>Find out more</span></div>
  <div class="ad-travel">
    <div class="logo">Tripwell</div>
    <div class="tag">Connecting TRAVELERS to DISCOUNTED TRAVEL DEALS</div>
    <div class="q">Traveling to Rio de Janeiro?</div>
    <div class="scene" role="img" aria-label="Mountain statue and a couple on a beach">
      <div class="sub">Corcovado Mountain, Christ Redeemer and Sugar Loaf Mountain Day Tour</div>
      <div class="was">Original Price $140</div>
      <div class="now">$70</div>
      <div class="off"><span>50%</span><span>OFF</span></div>
    </div>
  </div>
  <div class="social-box">
    <div class="t">Find us on Socialpage</div>
    <div class="who"><i></i><span>midlifers.com<br>1,933 people like Midlifers.com</span></div>
    <div class="faces" role="img" aria-label="Grid of follower profile photos"><i></i><i></i><i></i><i></i><i></i><i></i><i></i><i></i><i></i><i></i><i></i><i></i><i></i><i></i><i></i></div>
  </div>
</aside>

<footer class="site-footer">
  <nav class="footer-nav"><a>Home</a><em>/</em><a>About Midlifers.com</a><em>/</em><a>Advertise</a><em>/</em><a>Privacy Policy</a><em>/</em><a>Useful Links</a><em>/</em><a>Privacy Policy</a><em>/</em><a>Terms and Conditions</a><em>/</em><a>Contact us</a></nav>
  <div class="footer-rule"></div>
  <div class="copyright">© 2013 midlifers.com. All rights reserved.</div>
  <div class="follow"><i></i><i></i><i></i></div>
</footer>
</body>
</html>
```